Redo of existing website www.stonvira.example

I would like it to look like the newer style website, with large images, less text. clean and modern looking. The new design should focus on call to action. ultimately that's what were looking for.Some features I would like to see we try to do good job of keeping up with our blog, and it is a good source of recent pictures of our work. I like four visitors to get the few pieces they're doing with a national brand or franchise pray. I like to stay far from the idea of a local one-man band with magnetic signs on his truck.
I think that clean beautiful images have the biggest impact. In my opinion most people don't read more than a couple lines of text. The text is more for search engines.
we are currently in the process of revising our logo as well, I will upload those files when I get them.
Please feel free to use content and images from our current website www.stonvira.example. we can purchase professional stock images if needed.
1. large call to action with easy contact form.
2. Blog roll on front page to showcase our recent work.
2. All social connect buttons.
Check out our reviews on ratewell!
My current websites
Www.stonvira.example
https://social.example/profile/604918273655102938417/about
www.socialpage.example/stonvira
http://www.blogsite.example/blog/curbguardian
https://microblog.example/Stonvira
websites I like the way they look.
http://quillpost.example/
http://www.cartwell.example/
http://www.brennickpaving.example/
http://www.tarmacways.example/
http://curbandcoatingworks.example/
Hello all,
I have just uploaded some images of our company mascot "Curb Guardian" and our new logo.
Project Deadline Extended
Reason: Death in family. Finally back to work.
Target Market(s)
We have 2 main groups of customers commercial and residential.
Commercial customers are Property owners and managers, operators of multi location business, restaurant, supermarket, banks, and are best source for repeat business
for Residential customers we provide driveway repair and driveway paving services.
for residential customers I would like to encourge the submission or pictures with the inquiry for a quick quote. Residential customers are typically a one time job but are a good source of referrals
I like how this website separates residential and commercial
http://www.glintcoatonline.example
Call

```html
<!DOCTYPE html>
<html lang="en">
<head>
<meta charset="utf-8">
<title>Stonvira</title>
<link rel="stylesheet" href="https://fonts.googleapis.com/css2?family=Arimo:wght@400;700&family=Audiowide&family=Questrial&display=swap">
<style>
:root{
  --green:#10c814;
  --ink:#222;
  --gray:#8a8a8a;
  --light:#f2f2f2;
  --footer:#343434;
  --black:#111;
}
*{margin:0;padding:0;box-sizing:border-box}
html,body{width:802px;height:1200px;overflow:hidden;background:#fff}
body{position:relative;font-family:"Arimo",Arial,sans-serif;color:var(--ink)}
a{color:inherit;text-decoration:none}

.site-header{position:absolute;left:0;top:0;width:802px;height:86px}
.brand{position:absolute;left:70px;top:28px;display:flex;align-items:center;gap:8px}
.brand-mark{width:14px;height:14px;background:var(--green)}
.brand-name{font-family:"Arimo",sans-serif;font-weight:700;font-size:22px;color:var(--green);line-height:24px}
.phone{position:absolute;left:580px;top:14px;display:flex;align-items:center;gap:6px;font-family:"Questrial",sans-serif;font-size:16px;color:var(--gray);letter-spacing:.8px}
.social{position:absolute;left:606px;top:47px;display:flex;gap:8px}
.social span{width:24px;height:24px;border-radius:50%;background:#8e8e8e;display:block}

.main-nav{position:absolute;left:0;top:86px;width:802px;height:28px;background:var(--green);border-bottom:3px solid var(--black)}
.main-nav ul{list-style:none;display:flex;height:25px;align-items:center;padding-left:67px}
.main-nav .home{width:49px;height:25px;background:var(--black);display:flex;align-items:center;justify-content:center}
.main-nav li{font-size:10.4px;color:#fff}
.main-nav li.item{padding:0 15.5px}
.main-nav li.item:first-of-type{padding-left:8px}

.hero{position:absolute;left:0;top:117px;width:802px;height:367px;background:linear-gradient(180deg,#7fb0e8 0%,#a9c6e6 28%,#9a948a 55%,#5a5752 100%)}
.hero-caption{position:absolute;left:66px;top:193px;width:352px;height:103px;background:rgba(30,30,30,.72);padding:15px 10px 0 11px}
.hero-caption h1{font-family:"Audiowide",sans-serif;font-weight:400;font-size:22px;color:var(--green);letter-spacing:.5px;line-height:24px}
.hero-caption p{font-size:10px;line-height:13.5px;color:#fff;margin-top:10px;letter-spacing:.2px;padding-right:16px}

.welcome-photo{position:absolute;left:67px;top:517px;width:212px;height:175px;background:linear-gradient(180deg,#9cc2e6 0%,#b8b4aa 45%,#3a3a38 100%)}
.welcome{position:absolute;left:296px;top:514px;width:446px}
.welcome h2{font-family:"Questrial",sans-serif;font-weight:400;font-size:24px;color:var(--gray);letter-spacing:2px}
.welcome h2 strong{font-family:"Arimo",sans-serif;font-weight:700;font-size:23px;color:var(--green);letter-spacing:1px}
.welcome p{font-size:9.6px;line-height:17.5px;color:#555;margin:8px 0 0 4px}
.btn-outline{display:inline-flex;align-items:center;justify-content:center;width:89px;height:30px;border:2px solid var(--green);font-size:10.4px;font-weight:700;color:#444;margin:12px 0 0 3px}

.services-band{position:absolute;left:0;top:742px;width:802px;height:213px;background:linear-gradient(90deg,#3a3630 0%,#6a5a48 35%,#4a4a44 65%,#2e2e2c 100%)}
.services-head{position:absolute;left:0;top:751px;width:802px;text-align:center;color:#fff}
.services-head h2{font-family:"Questrial",sans-serif;font-weight:400;font-size:22px;letter-spacing:.8px;display:inline-block;padding:0 26px 2px;border-bottom:2px solid #fff}
.services-head p{font-size:9.6px;line-height:14.5px;width:600px;margin:7px auto 0}

.card{position:absolute;top:843px;width:205px;height:245px;background:var(--light);border-bottom:3px solid var(--green)}
.card-photo{height:112px;border:2px solid #fff}
.card h3{font-family:"Questrial",sans-serif;font-weight:400;font-size:14px;letter-spacing:.5px;color:#333;margin:9px 0 0 6px}
.card p{font-size:7.6px;line-height:16px;color:#222;margin:3px 6px 0 6px}
.btn-solid{display:inline-flex;align-items:center;justify-content:center;width:61px;height:19px;background:var(--green);color:#fff;font-size:9.6px;border-radius:2px;margin:5px 0 0 7px}
.card-1{left:66px}.card-1 .card-photo{background:linear-gradient(180deg,#88b4dc 0%,#6f8a5a 40%,#222 100%)}
.card-2{left:300px}.card-2 .card-photo{background:linear-gradient(160deg,#7a9a5a 0%,#2a2a2a 45%,#1b1b1b 100%)}
.card-3{left:532px}.card-3 .card-photo{background:linear-gradient(180deg,#b9c4cc 0%,#e8e8e8 55%,#d9b24a 80%,#eee 100%)}

.site-footer{position:absolute;left:0;top:1103px;width:802px;height:97px;background:var(--footer);color:#fff}
.footer-nav{position:absolute;left:70px;top:44px;display:flex;gap:14px;font-size:8px;letter-spacing:.2px}
.copyright{position:absolute;left:69px;top:66px;font-size:8.8px}
.footer-brand{position:absolute;left:560px;top:36px;display:flex;align-items:center;gap:8px}
.footer-brand .brand-name{font-size:21px}
</style>
</head>
<body>

<header class="site-header">
  <div class="brand">
    <span class="brand-mark"></span>
    <span class="brand-name">STONVIRA</span>
  </div>
  <div class="phone">
    <svg width="20" height="18" viewBox="0 0 20 18" aria-hidden="true"><path d="M2 6c0-3 16-3 16 0v2h-4V6c-2-1-6-1-8 0v2H2z" fill="var(--green)"/><path d="M5 9h10l2 8H3z" fill="var(--green)"/><circle cx="10" cy="13" r="2.4" fill="#fff"/></svg>
    <span>(555) 014 2790</span>
  </div>
  <div class="social" aria-label="Social links"><span></span><span></span><span></span><span></span></div>
</header>

<nav class="main-nav">
  <ul>
    <li class="home"><svg width="14" height="12" viewBox="0 0 14 12" aria-hidden="true"><path d="M7 0L0 6h2v6h4V8h2v4h4V6h2z" fill="#fff"/></svg></li>
    <li class="item">COMMERCIAL</li>
    <li class="item">RESIDENTIAL</li>
    <li class="item">ABOUT US</li>
    <li class="item">FREE ESTIMATE</li>
    <li class="item">TESTIMONIALS</li>
    <li class="item">BLOG</li>
  </ul>
</nav>

<section class="hero" role="img" aria-label="Crew patching asphalt in a snowy retail parking lot">
  <div class="hero-caption">
    <h1>LOREM IPSUM DOLOR</h1>
    <p>sed do eiusmod tempor incididunt ut labore et dolore magna aliqua. Ut enim ad minim veniam,ullamco laboris nisi ut aliquip ex ea commodo consequat.</p>
  </div>
</section>

<div class="welcome-photo" role="img" aria-label="Paving crew working beside an asphalt paver"></div>
<section class="welcome">
  <h2>WELCOME TO <strong>STONVIRA</strong></h2>
  <p>Lorem ipsum dolor sit amet, consectetur adipiscing elit, sed do eiusmod tempor incididunt ut labore et dolore magna aliqua. Ut enim ad minim veniam, quis nostrud exercitation ullamco laboris nisi ut aliquip ex ea commodo consequat. Duis aute irure dolor in reprehenderit in voluptate velit esse cillum dolore eu fugiat nulla pariatur Sed ut perspiciatis unde omnis iste natus error sit voluptatem accusantium doloremque laudantium, totam rem aperiam, eaque ipsa quae ab illo inventore veritatis et quasi architecto beatae vitae dicta sunt explicabo..</p>
  <a class="btn-outline" href="#">LEARN MORE</a>
</section>

<div class="services-band" role="img" aria-label="Blurred close-up of asphalt work"></div>
<div class="services-head">
  <h2>Lorem ipsum dolor sit amet</h2>
  <p>consectetur adipiscing elit, sed do eiusmod tempor incididunt ut labore et dolore magna aliqua. Ut enim ad minim veniam, quis nostrud exercitation ullamco laboris nisi ut aliquip ex ea commodo consequat.</p>
</div>

<article class="card card-1">
  <div class="card-photo" role="img" aria-label="Crew laying fresh asphalt on a street"></div>
  <h3>LOREM IPSUM</h3>
  <p>Lorem ipsum dolor sit amet, consectetur adipiscing elit, sed do eiusmod tempor incididunt ut labore et dolore magna aliqua. Ut enim ad minim veniam, aliquip ex ea commodo consequat.</p>
  <a class="btn-solid" href="#">View More</a>
</article>
<article class="card card-2">
  <div class="card-photo" role="img" aria-label="Freshly striped parking lot"></div>
  <h3>LOREM IPSUM</h3>
  <p>Lorem ipsum dolor sit amet, consectetur adipiscing elit, sed do eiusmod tempor incididunt ut labore et dolore magna aliqua. Ut enim ad minim veniam, aliquip ex ea commodo consequat.</p>
  <a class="btn-solid" href="#">View More</a>
</article>
<article class="card card-3">
  <div class="card-photo" role="img" aria-label="Skid loader clearing snow from a lot"></div>
  <h3>LOREM IPSUM</h3>
  <p>Lorem ipsum dolor sit amet, consectetur adipiscing elit, sed do eiusmod tempor incididunt ut labore et dolore magna aliqua. Ut enim ad minim veniam, aliquip ex ea commodo consequat.</p>
  <a class="btn-solid" href="#">View More</a>
</article>

<footer class="site-footer">
  <nav class="footer-nav">
    <span>HOME</span><span>COMMERCIAL</span><span>RESIDENTIAL</span><span>ABOUT US</span><span>FREE ESTIMATE</span><span>TESTIMONIALS</span><span>BLOG</span>
  </nav>
  <p class="copyright">Copyright © 2014 All Rights Reserved | Privacy Policy</p>
  <div class="footer-brand">
    <span class="brand-mark"></span>
    <span class="brand-name">STONVIRA</span>
  </div>
</footer>

</body>
</html>
```